Heater product information sheets

I need the two product information sheets organized and laid out in a clean, easy to read attractive manner. These sheets are to advertise propane heaters for outdoor use and for wholesale to propane distributors, restaurants and homeowners that need to have propane heat as the winter ends and spring begins. They will be used for chilly evenings when people want to be outside eating, drinking and being social.
Updates

Low design quality

Target Market(s)

Restaurants, hospitality industry, special events, party rental companies, home owners with backyards

Font styles to use
Sans Serif

Requirements
Must have
• My logo in the document instead of k. Dahlby and company
Nice to have
• I would like to see Fire illustrated coming up the heaters and on the round glass, show it up the middle of the glass tube propane heater.

```html
<!DOCTYPE html>
<html lang="en">
<head>
<meta charset="utf-8">
<title>Propane Heater Product Sheets</title>
<link href="https://fonts.googleapis.com/css2?family=Open+Sans:wght@400;600;700;800&family=Roboto+Condensed:wght@700&display=swap" rel="stylesheet">
<style>
:root{
  --backdrop:#575756;
  --paper:#ffffff;
  --orange:#ef7f1a;
  --orange-dark:#b85a1e;
  --charcoal:#3f3f3f;
  --ink:#2b2b2b;
  --frame:#8a8a8a;
  --white:#ffffff;
}
*{margin:0;padding:0;box-sizing:border-box}
html,body{width:1200px;height:994px;overflow:hidden;background:var(--backdrop)}
body{position:relative;font-family:"Open Sans",sans-serif;color:var(--ink)}
.sheet{position:absolute;top:124px;width:520px;height:734px;background:var(--paper);overflow:hidden}
.sheet--standard{left:53px}
.sheet--glass{left:614px}
.abs{position:absolute}
.title-frame{left:47px;top:24px;width:422px;height:52px;border:1.5px solid var(--frame)}
.title-bar{left:32px;top:32px;width:453px;height:38px;background:linear-gradient(90deg,var(--orange-dark),var(--orange));
  color:var(--white);font-weight:800;font-size:21px;letter-spacing:.5px;display:flex;align-items:center;justify-content:center;white-space:nowrap}
.uses{left:36px;top:86px;font-size:12px;font-weight:600;text-transform:uppercase;line-height:14px}
.uses li{list-style:none;position:relative;padding-left:20px;margin-bottom:4px}
.uses li::before{content:"";position:absolute;left:0;top:2px;width:10px;height:10px;border-radius:50%;background:var(--orange)}
.pill{left:32px;height:29px;padding:0 12px 0 16px;background:var(--orange);color:var(--white);font-weight:700;font-size:14px;
  letter-spacing:.2px;white-space:nowrap;border-radius:0 15px 15px 0;display:flex;align-items:center;border-left:2px solid var(--charcoal)}
.pill--spec{top:164px;width:188px}
.pill--details{top:295px;width:188px}
.pill--note{top:607px;width:86px;font-size:17px;padding-left:18px}
.checks{left:36px;font-size:12px;line-height:14px;list-style:none}
.checks li{position:relative;padding-left:20px;margin-bottom:5px}
.checks li svg{position:absolute;left:0;top:1px;width:10px;height:10px}
.checks--spec{top:203px;width:262px}
.checks--details{top:335px;width:292px}
.checks--details li{margin-bottom:6px}
.heater-photo{top:92px;height:510px;border-radius:40px 40px 8px 8px;z-index:1}
.sheet--standard .heater-photo{left:330px;width:140px;background:linear-gradient(180deg,#d9d9d9 0%,#bdbdbd 15%,#1f1f1f 35%,#111 100%)}
.sheet--glass .heater-photo{left:330px;width:150px;background:linear-gradient(180deg,#d9d9d9 0%,#e8e8e8 40%,#1c1c1c 60%,#111 100%)}
.footer-shape{left:0;top:540px}
.note-lines{left:32px;top:653px;font-family:"Roboto Condensed",sans-serif;font-weight:700;font-size:12.5px;line-height:19px;color:var(--white);white-space:nowrap}
.note-lines .label{color:var(--orange)}
.divider{left:268px;top:614px;height:94px;border-left:1.5px dotted var(--orange)}
.contact{left:284px;top:614px;color:var(--white);white-space:nowrap}
.contact h3{font-size:13px;font-weight:800;line-height:16px}
.contact .company{color:var(--orange);font-size:13px;font-weight:800;line-height:16px;text-transform:uppercase}
.contact ul{list-style:none;margin-top:5px;font-family:"Roboto Condensed",sans-serif;font-weight:700;font-size:12.5px}
.contact li{position:relative;padding-left:29px;height:19px;line-height:19px}
.contact li svg{position:absolute;left:0;top:3px;width:13px;height:13px}
</style>
</head>
<body>

<svg width="0" height="0" style="position:absolute">
  <symbol id="tick" viewBox="0 0 10 10"><circle cx="5" cy="5" r="4.2" fill="none" stroke="#ef7f1a" stroke-width="1"/><path d="M2.8 5.1l1.6 1.6L8.6 2.3" fill="none" stroke="#ef7f1a" stroke-width="1.2"/></symbol>
  <symbol id="phone" viewBox="0 0 13 13"><circle cx="6.5" cy="6.5" r="6.5" fill="#ef7f1a"/><path d="M4.2 3.3l1.3 1.5-.7.9c.5 1 1.2 1.7 2.2 2.2l.9-.7 1.5 1.3-.8 1.2C6.3 9.5 3.9 7.1 3.2 4.2z" fill="#fff"/></symbol>
  <symbol id="mail" viewBox="0 0 13 13"><circle cx="6.5" cy="6.5" r="6.5" fill="#ef7f1a"/><rect x="3.4" y="4.3" width="6.2" height="4.4" fill="#fff"/><path d="M3.4 4.3l3.1 2.4 3.1-2.4" fill="none" stroke="#ef7f1a" stroke-width=".7"/></symbol>
  <symbol id="pin" viewBox="0 0 13 13"><circle cx="6.5" cy="6.5" r="6.5" fill="#ef7f1a"/><path d="M6.5 2.8a2.5 2.5 0 0 1 2.5 2.5c0 1.8-2.5 4.6-2.5 4.6S4 7.1 4 5.3a2.5 2.5 0 0 1 2.5-2.5z" fill="#fff"/><circle cx="6.5" cy="5.3" r=".9" fill="#ef7f1a"/></symbol>
</svg>

<section class="sheet sheet--standard">
  <div class="abs title-frame"></div>
  <h1 class="abs title-bar">OUTDOOR PROPANE HEATER</h1>
  <ul class="abs uses">
    <li>Rentals for live events</li>
    <li>Rentals for restaurants &amp;<br>catering halls</li>
    <li>Purchase for your home or business</li>
  </ul>
  <h2 class="abs pill pill--spec">SPECIFICATIONS</h2>
  <ul class="abs checks checks--spec">
    <li><svg><use href="#tick"/></svg>Powerful 48,000 BTU</li>
    <li><svg><use href="#tick"/></svg>Black Powder Coated Finish</li>
    <li><svg><use href="#tick"/></svg>Uses 20 lbs. Propane Tank</li>
    <li><svg><use href="#tick"/></svg>CE, GS, AGA, CSA, with ETL certificate and ROHS approved.</li>
  </ul>
  <h2 class="abs pill pill--details">ADDITIONAL DETAILS</h2>
  <ul class="abs checks checks--details">
    <li><svg><use href="#tick"/></svg>Commercial Quality</li>
    <li><svg><use href="#tick"/></svg>For Outdoor Use Only</li>
    <li><svg><use href="#tick"/></svg>Safety Auto Shut Off Switch</li>
    <li><svg><use href="#tick"/></svg>Conforms to ANSI STD Z83.26-2014 Certified to CSA STD 2.37-2014 Gas- fired outdoor infrared patio heaters</li>
    <li><svg><use href="#tick"/></svg>Thermostatic Control</li>
    <li><svg><use href="#tick"/></svg>Base Diameter 17” - Anti-Tip Design</li>
    <li><svg><use href="#tick"/></svg>Standard Wheels - Tilt &amp; Move</li>
    <li><svg><use href="#tick"/></svg>88” Tall</li>
    <li><svg><use href="#tick"/></svg>Run time: 8-10 hours with standard 20 lbs. Propane tank</li>
    <li><svg><use href="#tick"/></svg>Heating Area: 200 sq. ft</li>
  </ul>
  <svg class="abs footer-shape" width="520" height="194" viewBox="0 0 520 194">
    <polygon points="0,51 520,8 520,194 0,194" fill="#ef7f1a"/>
    <polygon points="0,54 520,30 520,194 0,194" fill="#3f3f3f"/>
  </svg>
  <div class="abs heater-photo" role="img" aria-label="Photo of a black outdoor propane patio heater with a steel reflector top"></div>
  <h2 class="abs pill pill--note">NOTE</h2>
  <p class="abs note-lines"><span class="label">Price:</span> Starting at $250 each<br>Assembly &amp; Delivery available upon request<br>Discounts for large quantity orders</p>
  <div class="abs divider"></div>
  <div class="abs contact">
    <h3>TO RENT OR PURCHASE:</h3>
    <p class="company">K. Dahlby &amp; Company</p>
    <ul>
      <li><svg><use href="#phone"/></svg>555-014-2290</li>
      <li><svg><use href="#mail"/></svg>Nora@KDeventrental.com</li>
      <li><svg><use href="#pin"/></svg>42 Orchard Lane Linden, NJ 07036</li>
    </ul>
  </div>
</section>

<section class="sheet sheet--glass">
  <div class="abs title-frame"></div>
  <h1 class="abs title-bar">GLASS TUBE PROPANE HEATERS</h1>
  <ul class="abs uses">
    <li>Rentals for live events</li>
    <li>Rentals for restaurants &amp;<br>catering halls</li>
    <li>Purchase for your home or business</li>
  </ul>
  <h2 class="abs pill pill--spec">SPECIFICATIONS</h2>
  <ul class="abs checks checks--spec">
    <li><svg><use href="#tick"/></svg>Powerful 48,000 BTU</li>
    <li><svg><use href="#tick"/></svg>Black Powder Coated Finish</li>
    <li><svg><use href="#tick"/></svg>Uses 20 lbs. Propane Tank</li>
    <li><svg><use href="#tick"/></svg>CE, GS, AGA, CSA, with ETL certificate and ROHS approved.</li>
  </ul>
  <h2 class="abs pill pill--details">ADDITIONAL DETAILS</h2>
  <ul class="abs checks checks--details">
    <li><svg><use href="#tick"/></svg>Commercial Quality</li>
    <li><svg><use href="#tick"/></svg>For Outdoor Use Only</li>
    <li><svg><use href="#tick"/></svg>Safety Auto Shut Off Switch</li>
    <li><svg><use href="#tick"/></svg>Conforms to ANSI STD Z83.26-2014 Certified to CSA STD 2.37-2014 Gas- fired outdoor infrared patio heaters</li>
    <li><svg><use href="#tick"/></svg>Thermostatic Control</li>
    <li><svg><use href="#tick"/></svg>Base Diameter 17” - Anti-Tip Design</li>
    <li><svg><use href="#tick"/></svg>Standard Wheels - Tilt &amp; Move</li>
    <li><svg><use href="#tick"/></svg>99” Tall</li>
    <li><svg><use href="#tick"/></svg>Run time: 8-10 hours with standard 20 lbs. Propane tank</li>
    <li><svg><use href="#tick"/></svg>Heating Area: 200 sq. ft</li>
  </ul>
  <svg class="abs footer-shape" width="520" height="194" viewBox="0 0 520 194">
    <polygon points="0,51 520,8 520,194 0,194" fill="#ef7f1a"/>
    <polygon points="0,54 520,30 520,194 0,194" fill="#3f3f3f"/>
  </svg>
  <div class="abs heater-photo" role="img" aria-label="Photo of a glass tube propane heater with wire guard and black base"></div>
  <h2 class="abs pill pill--note">NOTE</h2>
  <p class="abs note-lines"><span class="label">Price:</span> Starting at $250 each<br>Assembly &amp; Delivery available upon request<br>Discounts for large quantity orders</p>
  <div class="abs divider"></div>
  <div class="abs contact">
    <h3>TO RENT OR PURCHASE:</h3>
    <p class="company">K. Dahlby &amp; Company</p>
    <ul>
      <li><svg><use href="#phone"/></svg>555-014-2290</li>
      <li><svg><use href="#mail"/></svg>Nora@KDeventrental.com</li>
      <li><svg><use href="#pin"/></svg>42 Orchard Lane Linden, NJ 07036</li>
    </ul>
  </div>
</section>

</body>
</html>
```